Business Card

Can you please copy the format provided for the business cards.
Can the logo be in the colours of the last file as specified.

Can the text please be in grey

• Navy Blue: #00457C
• Grey Text: #555555
• Orange Text: #FDBF29

The names on the business card will be

Dorian Platt
0452 718 340
dorian.platt@ridgelineassetlending.com.au

Lvl 7, 14 Harbourview Pde
Merrivale QLD 4290
PO Box 3472
Tarrin Vale MC QLD 9781
P: 1300 462 519
F: 1300 462 538
www.ridgelineassetlending.com.au

And

Liam Hollis
0437 915 604
liam.hollis@ridgelineassetlending.com.au

Lvl 7, 14 Harbourview Pde
Merrivale QLD 4290
PO Box 3472
Tarrin Vale MC QLD 9781
P: 1300 462 519
F: 1300 471 926

Industry/Entity Type

Business

```html
<!DOCTYPE html>
<html lang="en">
<head>
<meta charset="utf-8">
<title>Ridgeline Asset Lending – Business Card</title>
<link rel="stylesheet" href="https://fonts.googleapis.com/css2?family=Source+Sans+3:wght@400;600;700&display=swap">
<style>
  :root {
    --navy: #00457C;
    --grey-text: #777777;
    --amber: #FDBF29;
    --card-bg: #FFFFFF;
  }
  html, body {
    margin: 0;
    padding: 0;
    width: 1200px;
    height: 728px;
    overflow: hidden;
    background: var(--card-bg);
  }
  .business-card {
    position: relative;
    width: 1200px;
    height: 728px;
    background: var(--card-bg);
    font-family: "Source Sans 3", "Segoe UI", Arial, sans-serif;
  }
  .brand {
    position: absolute;
    left: 100px;
    top: 124px;
    display: flex;
    align-items: center;
    gap: 50px;
  }
  .brand-mark {
    width: 110px;
    height: 110px;
    background: var(--navy);
  }
  .brand-name {
    margin: 0;
    font-size: 46px;
    font-weight: 700;
    line-height: 1;
    color: var(--navy);
    letter-spacing: 0.5px;
  }
  .contact {
    position: absolute;
    left: 87px;
    top: 488px;
    color: var(--grey-text);
  }
  .contact-name {
    margin: 0 0 12px;
    font-size: 45px;
    font-weight: 600;
    line-height: 1;
  }
  .contact-phone {
    margin: 0 0 14px;
    font-size: 42px;
    font-weight: 400;
    line-height: 1;
    letter-spacing: 0.5px;
  }
  .contact-email {
    margin: 0;
    font-size: 32px;
    font-weight: 400;
    line-height: 1;
  }
</style>
</head>
<body>
  <main class="business-card">
    <header class="brand">
      <div class="brand-mark" aria-hidden="true"></div>
      <p class="brand-name">Ridgeline Asset Lending</p>
    </header>
    <section class="contact">
      <p class="contact-name">Liam Hollis</p>
      <p class="contact-phone">0437 915 604</p>
      <p class="contact-email">liam.hollis@ridgelineassetlending.com.au</p>
    </section>
  </main>
</body>
</html>
```